Business Card Design

Motorvane Ledger is an online automotive resource on a national scale specifically targeting lease purchases for new cars. Our Online and app platform allow prospective lease clients to scan a window sticker while at a franchise dealership and instantly receive a lease quote at what we call the sweet spot. Motorvane Ledger offers price transparency during the lease process to allow average people the confidence in the lease process and takes away any fear of the big franchise dealers.
Motorvane ledger allows ordinary lease customers to know they are getting a low price lease and not overpaying. Never overpay again

Industry/Entity Type

Automotive

Contact Information for Business Card

Motorvane Ledger
Martin Sowerby (President of operations)
Phone: 888-247-6031
Cell: 561-384-2706

```html
<!DOCTYPE html>
<html lang="en">
<head>
<meta charset="utf-8">
<title>Motorvane Ledger – Business Card</title>
<link href="https://fonts.googleapis.com/css2?family=Montserrat:wght@400;600;800&display=swap" rel="stylesheet">
<style>
  :root {
    --stage: #d9d9d9;
    --card: #111111;
    --card-edge: #1c1c1c;
    --band: #444444;
    --accent: #1a9ad6;
    --ink-light: #ffffff;
    --ink-muted: #bdbdbd;
  }
  * { margin: 0; padding: 0; box-sizing: border-box; }
  html, body {
    width: 1200px; height: 861px; overflow: hidden;
    background: var(--stage);
    font-family: "Montserrat", Arial, sans-serif;
  }
  .sheet {
    position: relative; width: 1200px; height: 861px;
    display: flex; align-items: center; justify-content: center; gap: 60px;
  }
  .card {
    position: relative; width: 520px; height: 298px;
    background: linear-gradient(135deg, var(--card-edge), var(--card));
    border-radius: 4px;
    box-shadow: 0 12px 30px rgba(0,0,0,0.25);
    overflow: hidden;
  }
  .brand {
    display: flex; align-items: center; gap: 10px;
    color: var(--ink-light); font-weight: 800; text-transform: uppercase;
  }
  .brand-dot { border-radius: 50%; background: var(--ink-light); flex: none; }
  .card-front .brand { position: absolute; left: 36px; top: 30px; font-size: 22px; }
  .card-front .brand-dot { width: 16px; height: 16px; }
  .holder { position: absolute; left: 36px; top: 76px; }
  .holder-name {
    color: var(--accent); font-weight: 600; font-size: 22px;
    text-transform: uppercase; letter-spacing: 0.5px;
  }
  .holder-role {
    color: var(--ink-muted); font-weight: 400; font-size: 11px;
    text-transform: uppercase; letter-spacing: 1.5px; margin-top: 2px;
  }
  .contact-list { position: absolute; left: 0; right: 0; top: 150px; list-style: none; }
  .contact-row {
    display: flex; align-items: center; height: 30px; margin-bottom: 10px;
    background: var(--band);
    color: var(--ink-light); font-size: 13px; font-weight: 600;
  }
  .contact-icon {
    width: 30px; height: 30px; margin-left: 36px; margin-right: 16px;
    background: var(--accent);
    display: flex; align-items: center; justify-content: center;
  }
  .contact-icon svg { width: 16px; height: 16px; fill: var(--card); }
  .card-back { display: flex; align-items: center; justify-content: center; }
  .card-back .brand { font-size: 36px; }
  .card-back .brand-dot { width: 26px; height: 26px; }
</style>
</head>
<body>
<main class="sheet">
  <section class="card card-front" aria-label="Card front">
    <div class="brand"><span class="brand-dot"></span>Motorvane Ledger</div>
    <div class="holder">
      <p class="holder-name">Martin Sowerby</p>
      <p class="holder-role">President of Operations</p>
    </div>
    <ul class="contact-list">
      <li class="contact-row">
        <span class="contact-icon"><svg viewBox="0 0 24 24" aria-hidden="true"><path d="M6.6 10.8a15 15 0 0 0 6.6 6.6l2.2-2.2c.3-.3.7-.4 1-.2 1.1.4 2.3.6 3.6.6.6 0 1 .4 1 1V20c0 .6-.4 1-1 1A17 17 0 0 1 3 4c0-.6.4-1 1-1h3.5c.6 0 1 .4 1 1 0 1.3.2 2.5.6 3.6.1.3 0 .7-.2 1z"/></svg></span>
        888-247-6031
      </li>
      <li class="contact-row">
        <span class="contact-icon"><svg viewBox="0 0 24 24" aria-hidden="true"><path d="M7 2h10a1 1 0 0 1 1 1v18a1 1 0 0 1-1 1H7a1 1 0 0 1-1-1V3a1 1 0 0 1 1-1zm1 3v13h8V5zm4 14.2a1 1 0 1 0 0 2 1 1 0 0 0 0-2z"/></svg></span>
        561-384-2706
      </li>
      <li class="contact-row">
        <span class="contact-icon"><svg viewBox="0 0 24 24" aria-hidden="true"><path d="M12 2a7 7 0 0 0-7 7c0 5 7 13 7 13s7-8 7-13a7 7 0 0 0-7-7zm0 9.5A2.5 2.5 0 1 1 12 6.5a2.5 2.5 0 0 1 0 5z"/></svg></span>
        480 Harbor Point Dr. Suite 12 Ashford Bay, FL 33901
      </li>
    </ul>
  </section>
  <section class="card card-back" aria-label="Card back">
    <div class="brand"><span class="brand-dot"></span>Motorvane Ledger</div>
  </section>
</main>
</body>
</html>
```